Business card for a boutique travel agency VELIRANDE

we need a business card design - double sided. We would like to have a very elegant, sophisticated but modern design. we are travel consultants and our business focus is Europe, mainly the city of Paris. We would like to receive designs in white and silver, black color but if you are confident that we should pick up a color to make it different and more beautful...go ahead! We are going to give business cards to our clients and business partners. It is important to be perceived as elegant, modern and trustful. Please check jpg references.

Target Market(s)

Velirande primary clients are individuals, couples and affinity groups of high-net-worth who travel for leisure at least once per year. Seeking the ultimate travel experience, the target clients demand the finest quality activities and accommodations accompanied by a superior level of service.

Industry/Entity Type

Travel Industry

Contact Information for Business Card

Liliana Quesada
- liliana@velirande-mail.example
- +55 11 98437.5216
- velirande-mail.example
- unique travel experiences (we would like to see this signature printed as a detail)

Font styles to use
Sans Serif

Colors

Designer to choose colors to be used in the design.

Requirements
Must have
• the Velirande logo that I have attached
Nice to have
• we would like to have some nice detail, something different that shows that we care about,... we are detail oriented.
Should not have
• decorative fonts

```html
<!DOCTYPE html>
<html lang="en">
<head>
<meta charset="utf-8">
<title>Velirande — Business Card</title>
<link href="https://fonts.googleapis.com/css2?family=Josefin+Sans:wght@300&family=Lato:wght@400&display=swap" rel="stylesheet">
<style>
  :root {
    --backdrop: #d9d9d7;
    --card: #1b1b1b;
    --card-light: #262626;
    --copper: #b98765;
    --copper-edge: #a8744f;
  }
  html, body {
    margin: 0;
    padding: 0;
    width: 1200px;
    height: 900px;
    overflow: hidden;
    background: var(--backdrop);
  }
  .canvas {
    position: relative;
    width: 1200px;
    height: 900px;
  }
  .card {
    position: absolute;
    left: 290px;
    width: 620px;
    height: 354px;
    background: radial-gradient(ellipse at 50% 30%, var(--card-light), var(--card) 70%);
    border-bottom: 3px solid var(--copper-edge);
    box-sizing: border-box;
    box-shadow: 0 10px 28px rgba(0,0,0,0.25);
  }
  .card--back { top: 70px; }
  .card--front { top: 476px; }

  .contact {
    position: absolute;
    left: 48px;
    bottom: 46px;
    font-family: "Lato", sans-serif;
    font-size: 13px;
    letter-spacing: 3px;
    text-transform: uppercase;
    color: var(--copper);
    line-height: 1.75;
  }
  .contact__name {
    margin: 0;
    font-size: 14px;
    letter-spacing: 4px;
  }
  .contact__rule {
    width: 110px;
    height: 1px;
    background: var(--copper);
    margin: 10px 0 12px;
    border: 0;
  }
  .contact__line { margin: 0; }

  .brand {
    position: absolute;
    inset: 0;
    display: flex;
    align-items: center;
    justify-content: center;
    font-family: "Josefin Sans", sans-serif;
    font-weight: 300;
    font-size: 46px;
    letter-spacing: 16px;
    color: var(--copper);
    padding-left: 16px;
  }
</style>
</head>
<body>
<main class="canvas">
  <section class="card card--back" aria-label="Card back">
    <div class="contact">
      <p class="contact__name">Liliana Quesada</p>
      <hr class="contact__rule">
      <p class="contact__line">+55 11 98437.5216</p>
      <p class="contact__line">liliana@velirande-mail.example</p>
      <p class="contact__line">www.velirande-mail.example</p>
    </div>
  </section>

  <section class="card card--front" aria-label="Card front">
    <div class="brand">VELIRANDE</div>
  </section>
</main>
</body>
</html>
```